Web Page for The Brannock Law Firm

The Brannock Law Firm, 7 Quillen Lane, Alma, Ga 31510 is a one lawyer trial firm specializing in sever personal injury, including auto accidents, trucking accidents, severe injuries from defective products. Mr Brannock also has been successfully trying these, commercial and business disputes, criminal cases and high net worth divorce cases for over 28 years. He has tried over 100 cases to a jury verdict.

Douglas is a member of all the trial courts of the State of Georgia, including the Northern, Middle and Southern District Federal Courts, the Georgia Court of Appeals, The Georgia Supreme Court, the 11th Circuit Federal Court of appeals and the United States Supreme Court. Douglas holds the largest verdict in South Georgia history of $150,000,000.00. He is a Member of the Peachvale Legal Standards Council and an active member of the Meridian Courtroom Advocates Guild.

Douglas R. Brannock graduated from Pinewick Valley High School in Alma, Georgia in 1978. He received his BBA in Accounting in 1982 and graduated cum laude from the Halloway Institute College of Law in 1986 with a J.D.

Industry/Entity Type

Lawyer

Number of Pages Required

4 page

Requirements
Must have
• Introduction to firm; separate biography of principal; representative cases; testemonials; blog; method of contact

```html
<!DOCTYPE html>
<html lang="en">
<head>
<meta charset="utf-8">
<title>The Brannock Law Firm</title>
<link href="https://fonts.googleapis.com/css2?family=Gelasio:wght@400;700&family=Open+Sans:ital,wght@0,400;0,600;0,700;1,400&family=Roboto:wght@700&display=swap" rel="stylesheet">
<style>
:root{
  --blue:#2f7fd6;
  --ink:#222;
  --line:#e3e3e3;
  --light:#f2f2f2;
  --dark:#1e1e1e;
  --darker:#050505;
  --green:#8cc152;
}
*{margin:0;padding:0;box-sizing:border-box}
html,body{width:1200px;height:2871px;overflow:hidden;background:#fff}
body{font-family:"Open Sans",sans-serif;color:var(--ink);position:relative}
.serif{font-family:"Gelasio",serif}
.abs{position:absolute}

/* top bar */
.topbar{position:absolute;top:0;left:0;width:1200px;height:38px;background:#f4f4f4;font-size:11px;color:#555}
.social{position:absolute;left:92px;top:12px;display:flex;gap:6px}
.social span{width:14px;height:14px;border-radius:50%;background:#cfcfcf;display:block}
.topbar .contact{position:absolute;left:650px;top:11px}
.topbar .mail{position:absolute;left:790px;top:11px;white-space:nowrap}
.search{position:absolute;left:980px;top:10px;width:128px;height:18px;background:#fff;border:1px solid #ddd;font-size:9px;color:#aaa;padding:2px 6px}
.search i{position:absolute;right:0;top:0;width:18px;height:16px;background:#ccc}

/* nav */
.nav{position:absolute;top:38px;left:0;width:1200px;height:77px;background:#fff}
.logo{position:absolute;left:90px;top:20px;display:flex;align-items:center;gap:10px;color:var(--blue);font-size:25px;font-weight:400}
.logo i{width:34px;height:34px;background:var(--blue);display:block}
.menu{position:absolute;right:88px;top:28px;display:flex;gap:32px;font-size:14px;color:#333}
.menu .on{color:var(--blue)}

/* hero */
.hero{position:absolute;top:115px;left:0;width:1200px;height:485px;background:linear-gradient(90deg,#3a3d42 0%,#6e7278 45%,#a8a59f 75%,#8b8e92 100%)}
.hero h1{position:absolute;left:92px;top:100px;font-family:"Roboto",sans-serif;font-size:62px;line-height:64px;color:#fff;font-weight:700}
.hero p{position:absolute;left:92px;top:235px;width:416px;background:rgba(0,0,0,.75);color:#fff;font-size:12.5px;line-height:20px;padding:4px 6px}
.btn{background:var(--blue);color:#fff;font-weight:700;text-align:center;border-radius:3px}
.hero .btn{position:absolute;left:92px;top:308px;width:172px;height:40px;line-height:40px;font-size:16px;letter-spacing:.5px}
.dots{position:absolute;left:564px;top:431px;display:flex;gap:6px}
.dots span{width:18px;height:18px;border-radius:50%;background:#fff;border:4px solid #111}
.dots span.on{border-color:var(--blue)}

/* welcome */
.welcome{position:absolute;top:600px;left:0;width:1200px;height:255px;text-align:center}
.welcome h2{margin-top:36px;font-size:28px;font-weight:400}
.welcome p{width:600px;margin:12px auto 0;font-size:13px;line-height:21px;color:#999}
.consult{position:absolute;top:152px;left:0;width:1200px;display:flex;justify-content:center;align-items:center;gap:30px;font-size:17px}
.consult .btn{width:226px;height:40px;line-height:40px;font-family:"Open Sans",sans-serif;font-size:20px;font-weight:600}

/* practice */
.practice{position:absolute;top:855px;left:0;width:1200px;height:514px;background:linear-gradient(180deg,#e4e4e4,#f6f6f6 60%,#ececec)}
.practice h2{text-align:center;font-size:28px;font-weight:400;margin-top:24px}
.rule{position:absolute;left:426px;top:84px;width:348px;height:1px;background:#222}
.rule i{position:absolute;left:168px;top:-6px;width:13px;height:13px;border-radius:50%;background:#111}
.tile{position:absolute;width:222px;height:158px;background:linear-gradient(160deg,#4d4f52,#2b2c2e)}
.tile svg{position:absolute;left:100px;top:54px}
.tile span{position:absolute;left:50%;top:78px;transform:translateX(-50%);white-space:nowrap;border:2px solid #fff;border-radius:14px;padding:2px 10px;color:#fff;font-family:"Gelasio",serif;font-size:14px;background:rgba(0,0,0,.35)}

/* testimonials */
.why{position:absolute;top:1400px;left:88px;font-size:29px;font-weight:400}
.quote{position:absolute;width:470px}
.avatar{position:absolute;left:0;top:0;width:52px;height:52px;border-radius:50%;background:linear-gradient(#c9b3a0,#8d6e5a);border:3px solid #eee}
.qbox{position:absolute;left:78px;top:0;width:398px;border:1px solid var(--line);padding:12px 18px 14px;font-size:11.5px;line-height:19px;color:#888}
.qbox em{display:block}
.qbox .who{margin-top:10px;font-style:normal;color:#555}
.qbox .who b{font-weight:400;color:var(--green)}

/* blog & video */
.sec-title{position:absolute;top:1816px;font-size:29px;font-weight:400}
.blog-img{position:absolute;left:88px;top:1878px;width:80px;height:86px;background:linear-gradient(#5a6b80,#2a3340)}
.blog-date{position:absolute;left:88px;top:1964px;width:80px;height:32px;background:#222;color:#fff;font-weight:700;font-size:22px;padding-left:14px;line-height:32px}
.blog-date small{font-size:10px;font-weight:400;margin-left:4px}
.blog-comm{position:absolute;left:88px;top:1996px;width:80px;height:26px;background:#efefef;font-size:11px;color:#999;padding:5px 0 0 20px}
.blog-body{position:absolute;left:168px;top:1878px;width:370px;height:270px;background:var(--light);padding:28px 30px}
.blog-body h3{font-weight:400;font-size:15px;line-height:20px;color:var(--blue)}
.blog-body p{margin-top:14px;font-size:11px;line-height:18.5px;color:#777}
.video{position:absolute;left:591px;top:1878px;width:521px;height:270px;border-radius:6px;background:linear-gradient(135deg,#e6e6e6,#b9bcc0 55%,#7d7f83)}
.video svg{position:absolute;left:212px;top:84px}

/* contact */
.contact-sec{position:absolute;top:2153px;left:0;width:1200px;height:450px;background:var(--dark);color:#fff}
.contact-sec h2{text-align:center;font-size:28px;font-weight:400;margin-top:24px}
.contact-sec .lead{text-align:center;font-family:"Gelasio",serif;font-size:18px;margin-top:4px}
.field{position:absolute;height:42px;background:#4a4a4a}
.field i{position:absolute;right:0;top:0;width:30px;height:42px;background:#3d3d3d}
.label{position:absolute;font-size:12px;color:#bbb}
.submit{position:absolute;left:484px;top:320px;width:213px;height:44px;line-height:44px;font-size:14px}

/* footer */
.info{position:absolute;top:2603px;left:0;width:1200px;height:201px;background:var(--darker);color:#fff}
.col{position:absolute;top:50px}
.col h4{font-family:"Gelasio",serif;font-size:18px;font-weight:400}
.col .av{font-size:15px;color:#666;font-family:"Gelasio",serif}
.col .big{font-size:20px;font-weight:600;margin-top:10px}
.col .small{font-family:"Gelasio",serif;font-size:13px;line-height:18px;margin-top:8px}
.divider{position:absolute;top:16px;width:1px;height:150px;background:#444}
.copy{position:absolute;top:2804px;left:0;width:1200px;height:67px;background:var(--blue);color:#fff;font-family:"Gelasio",serif;font-size:12px}
.copy .l{position:absolute;left:88px;top:26px}
.copy .r{position:absolute;right:102px;top:26px}
</style>
</head>
<body>

<header class="topbar">
  <div class="social"><span></span><span></span><span></span><span></span><span></span></div>
  <div class="contact">Call Us: (555) 010-4782</div>
  <div class="mail">Email: hello@brannocklaw.com</div>
  <div class="search">Search...<i></i></div>
</header>

<nav class="nav">
  <div class="logo"><i></i>Brannock Law Firm</div>
  <div class="menu"><span class="on">Home</span><span>About Firm</span><span>Attorneys</span><span>Practice Areas</span><span>Features</span><span>Blog</span><span>Contact</span></div>
</nav>

<section class="hero" role="img" aria-label="Photo of attorneys meeting with clients around a conference table">
  <h1>NEED LEGAL<br>ASSISTANCES?</h1>
  <p>Get Immediate free information and advice confidential from the experienced attorneys on most common legal issues.</p>
  <div class="btn">LEARN MORE</div>
  <div class="dots"><span class="on"></span><span></span><span></span></div>
</section>

<section class="welcome">
  <h2 class="serif">WELCOME TO LAW FIRM - PROVIDING LEGAL HELP</h2>
  <p>We stand beside injured people and businesses in every court of the state, preparing each case for trial from the very first day, with honest advice and steady care.</p>
  <div class="consult serif"><span>Get your Free Consultation</span><span class="btn">(555) 010-4782</span><span>Available 24/7</span></div>
</section>

<section class="practice">
  <h2 class="serif">PRACTICE AREAS</h2>
  <div class="rule"><i></i></div>

  <div class="tile" style="left:134px;top:123px" role="img" aria-label="Photo of an injured person receiving care">
    <svg width="22" height="18" viewBox="0 0 22 18"><path d="M8 1h6v5h5v6h-5v5H8v-5H3V6h5z" fill="#fff"/></svg>
    <span>Personal Injury</span></div>
  <div class="tile" style="left:371px;top:123px" role="img" aria-label="Photo of a damaged car">
    <svg width="22" height="18" viewBox="0 0 22 18"><path d="M3 9 L6 3 H16 L19 9 V15 H3 Z" fill="#fff"/><circle cx="7" cy="15" r="2" fill="#333"/><circle cx="15" cy="15" r="2" fill="#333"/></svg>
    <span>Auto Accidents</span></div>
  <div class="tile" style="left:608px;top:123px" role="img" aria-label="Photo of a truck on a highway">
    <svg width="22" height="18" viewBox="0 0 22 18"><rect x="1" y="3" width="13" height="10" fill="#fff"/><path d="M14 6h4l3 4v3h-7z" fill="#fff"/><circle cx="5" cy="15" r="2" fill="#fff"/><circle cx="17" cy="15" r="2" fill="#fff"/></svg>
    <span>Trucking Accidents</span></div>
  <div class="tile" style="left:845px;top:123px" role="img" aria-label="Photo of a faulty product">
    <svg width="22" height="18" viewBox="0 0 22 18"><path d="M11 1 L21 17 H1 Z" fill="#fff"/><rect x="10" y="6" width="2" height="6" fill="#333"/><rect x="10" y="13" width="2" height="2" fill="#333"/></svg>
    <span>Defective Products</span></div>

  <div class="tile" style="left:134px;top:296px" role="img" aria-label="Photo of business people in discussion">
    <svg width="22" height="18" viewBox="0 0 22 18"><rect x="1" y="5" width="20" height="12" fill="#fff"/><rect x="7" y="1" width="8" height="5" fill="none" stroke="#fff" stroke-width="2"/></svg>
    <span>Business Disputes</span></div>
  <div class="tile" style="left:371px;top:296px" role="img" aria-label="Photo of a courtroom">
    <svg width="22" height="18" viewBox="0 0 22 18"><path d="M11 1 L21 5 H1 Z" fill="#fff"/><rect x="3" y="6" width="2" height="8" fill="#fff"/><rect x="8" y="6" width="2" height="8" fill="#fff"/><rect x="12" y="6" width="2" height="8" fill="#fff"/><rect x="17" y="6" width="2" height="8" fill="#fff"/><rect x="1" y="15" width="20" height="2" fill="#fff"/></svg>
    <span>Criminal Defense</span></div>
  <div class="tile" style="left:608px;top:296px" role="img" aria-label="Photo of a family walking outdoors">
    <svg width="22" height="18" viewBox="0 0 22 18"><circle cx="6" cy="5" r="3" fill="#fff"/><circle cx="16" cy="5" r="3" fill="#fff"/><rect x="2" y="9" width="8" height="8" rx="3" fill="#fff"/><rect x="12" y="9" width="8" height="8" rx="3" fill="#fff"/></svg>
    <span>High Net Worth Divorce</span></div>
  <div class="tile" style="left:845px;top:296px" role="img" aria-label="Photo of hands over legal papers">
    <svg width="22" height="18" viewBox="0 0 22 18"><rect x="3" y="3" width="13" height="14" fill="none" stroke="#fff" stroke-width="2"/><path d="M10 12 L19 2 L21 4 L12 14 Z" fill="#fff"/></svg>
    <span>Other Cases</span></div>
</section>

<h2 class="why serif">Why Clients Love Us</h2>

<div class="quote" style="left:92px;top:1468px">
  <div class="avatar" role="img" aria-label="Client portrait"></div>
  <div class="qbox"><em>Douglas kept us informed at every step and never rushed a single question. His preparation for trial was thorough and the result exceeded all we had hoped for.</em><div class="who">- Lena Hartwell / <b>Ridgeford Co</b></div></div>
</div>
<div class="quote" style="left:626px;top:1468px">
  <div class="avatar" role="img" aria-label="Client portrait"></div>
  <div class="qbox"><em>After the truck accident we felt lost. The firm handled everything with patience and care, and we finally felt heard. Truly grateful for all the help.</em><div class="who">- Lena Hartwell / <b>Ridgeford Co</b></div></div>
</div>
<div class="quote" style="left:92px;top:1626px">
  <div class="avatar" role="img" aria-label="Client portrait"></div>
  <div class="qbox"><em>Clear advice, honest answers and a steady hand in court. Our business dispute was settled fairly and far sooner than we ever expected it would be.</em><div class="who">- Lena Hartwell / <b>Ridgeford Co</b></div></div>
</div>
<div class="quote" style="left:626px;top:1626px">
  <div class="avatar" role="img" aria-label="Client portrait"></div>
  <div class="qbox"><em>From our first call to the verdict he treated our family with respect. I would recommend this firm to anyone facing a serious injury claim.</em><div class="who">- Lena Hartwell / <b>Ridgeford Co</b></div></div>
</div>

<h2 class="sec-title serif" style="left:88px">Recent Blogs</h2>
<h2 class="sec-title serif" style="left:590px">Our Videos</h2>

<div class="blog-img" role="img" aria-label="Photo of an attorney in a suit"></div>
<div class="blog-date">25<small>NOV</small></div>
<div class="blog-comm">
  <svg class="abs" style="left:4px;top:6px" width="14" height="12" viewBox="0 0 14 12"><path d="M1 1h12v7H6l-3 3V8H1z" fill="#999"/></svg>450</div>
<div class="blog-body">
  <h3>Publishing packages and web page editors now use as their default model text.</h3>
  <p>Most injury claims are won or lost in the first weeks after an accident. Keep every medical record, take photos of the scene, write down names of witnesses and avoid giving statements to insurers before you speak with counsel. Small steps taken early protect the value of your case and give your attorney the facts needed to build a strong claim for trial.</p>
</div>
<div class="video" role="img" aria-label="Video still of attorneys in a meeting">
  <svg width="96" height="96" viewBox="0 0 96 96"><circle cx="48" cy="48" r="44" fill="none" stroke="#fff" stroke-width="6"/><path d="M38 28 L68 48 L38 68 Z" fill="#fff"/></svg>
</div>

<section class="contact-sec">
  <h2 class="serif">Need Legal Assistance - Do You Have a Claim?</h2>
  <p class="lead">Feel free to get in touch with any enquiries and one of our friendly members of staff will get back to you as soon as possible.</p>
  <span class="label" style="left:126px;top:100px">Your Name*</span>
  <div class="field" style="left:126px;top:120px;width:293px"><i></i></div>
  <span class="label" style="left:444px;top:100px">Your E-mail*</span>
  <div class="field" style="left:444px;top:120px;width:293px"><i></i></div>
  <span class="label" style="left:760px;top:100px">Phone Number</span>
  <div class="field" style="left:760px;top:120px;width:293px"><i></i></div>
  <span class="label" style="left:126px;top:177px">Message*</span>
  <div class="field" style="left:126px;top:197px;width:927px;height:90px"><i style="height:30px"></i></div>
  <div class="btn submit">Submit Your Message</div>
</section>

<footer class="info">
  <div class="col" style="left:92px"><h4>Get Free Consultation</h4><div class="av">Available 24/7</div><div class="big">(555) 010-4782</div></div>
  <div class="divider" style="left:347px"></div>
  <div class="col" style="left:422px"><h4>Message Us Now</h4><div class="av">Available 24/7</div><div class="big">info@brannock.com</div></div>
  <div class="divider" style="left:653px"></div>
  <div class="col" style="left:700px"><h4>Address Location</h4><div class="small">7 Quillen Lane, Alma, GA 31510<br>Fax: (555) 010-4783<br>View Map</div></div>
</footer>
<div class="copy"><span class="l">Copyright © 2014 The Brannock Law Firm. All Rights Reserved</span><span class="r">Notices | Privacy Policy | Careers | Site MapScroll</span></div>

</body>
</html>
```